Business card design for Automotive workshop

We need a business card for a new automotive repair and tyre shop called Ridgeback Prime Automotive located in New Zealand. We are a clean, modern and fresh workshop and company.

Front needs to feature logo,
my name:
Lachie Westergaard (director)

Address:
48 Marlow Lane
Kereru Bay 3592

Phone: 07 842 1937
Mobile: 027 519 2764
Email: office@ridgebackmotors.co.nz
Website: ridgebackmotors.co.nz

Back needs to feature an area to write down appointment details, date and time.

Also feature a list of jobs and work we do such as,
Vehicle Servicing
All Mechanical Repairs
Warrant of Fitness
Tyres & Wheel Alignments
Automotive Diagnostics
Automotive Parts & Supplies

```html
<!DOCTYPE html>
<html lang="en">
<head>
<meta charset="utf-8">
<title>Ridgeback Prime Automotive – Business Card</title>
<link href="https://fonts.googleapis.com/css2?family=PT+Sans:wght@400;700&family=PT+Sans+Narrow:wght@700&display=swap" rel="stylesheet">
<style>
  :root {
    --backdrop: #d4d6d6;
    --card-light: #ffffff;
    --card-dark: #232323;
    --brand-red: #e31b23;
    --ink: #3a3a3a;
    --ink-soft: #555555;
    --paper-text: #f2f2f2;
    --rule-dark: #4a4a4a;
  }
  * { margin: 0; padding: 0; box-sizing: border-box; }
  html, body {
    width: 1200px; height: 900px; overflow: hidden;
    background: var(--backdrop);
    font-family: "PT Sans", Arial, sans-serif;
  }
  .canvas { position: relative; width: 1200px; height: 900px; }

  .card {
    position: absolute;
    width: 540px; height: 310px;
    box-shadow: 0 6px 14px rgba(0,0,0,0.18);
  }

  .brand {
    display: flex; align-items: center; gap: 10px;
    font-weight: 700; color: var(--brand-red);
    letter-spacing: 0.5px; text-transform: uppercase;
    white-space: nowrap;
  }
  .brand__mark { width: 14px; height: 14px; background: var(--brand-red); flex: none; }

  /* Appointment side */
  .card--appointment {
    left: 60px; top: 110px;
    background: var(--card-light);
    color: var(--ink);
    padding: 30px 40px 24px;
    display: flex; flex-direction: column; align-items: center;
  }
  .card--appointment .brand { font-size: 23px; }
  .appointment-title {
    margin-top: 10px;
    font-weight: 700; font-size: 17px; color: var(--brand-red);
    letter-spacing: 0.5px;
  }
  .appointment-rows { width: 100%; margin-top: 12px; }
  .appointment-row {
    display: flex; align-items: flex-end; gap: 8px;
    font-size: 13px; margin-bottom: 14px;
  }
  .appointment-row__line { border-bottom: 1px solid var(--ink); height: 1px; }
  .appointment-row__line--date { flex: 2.4; }
  .appointment-row__line--time { flex: 1; }
  .services {
    margin-top: auto;
    font-size: 13px; color: var(--ink-soft); text-align: center; line-height: 1.35;
  }
  .services .dot { color: var(--brand-red); }

  /* Contact side */
  .card--contact {
    left: 600px; top: 480px;
    background: var(--card-dark);
    color: var(--paper-text);
    padding: 48px 36px 30px;
  }
  .card--contact .brand { font-size: 25px; justify-content: center; }
  .contact-body {
    display: flex; margin-top: 62px; gap: 22px;
  }
  .person { flex: 1; text-align: right; }
  .person__name {
    font-family: "PT Sans Narrow", "Arial Narrow", sans-serif;
    font-weight: 700; font-size: 24px; color: var(--brand-red); line-height: 1;
  }
  .person__role { font-size: 13px; margin-top: 4px; }
  .person__address { font-size: 13px; margin-top: 20px; }
  .divider { width: 1px; background: var(--rule-dark); }
  .contact-list { flex: 1.15; list-style: none; font-size: 13px; }
  .contact-list li { display: flex; align-items: center; gap: 8px; margin-bottom: 6px; }
  .contact-list svg { width: 12px; height: 12px; flex: none; }
</style>
</head>
<body>
<main class="canvas">

  <section class="card card--appointment" aria-label="Appointment side">
    <div class="brand"><span class="brand__mark"></span>Ridgeback Prime Automotive</div>
    <div class="appointment-title">APPOINTMENT</div>
    <div class="appointment-rows">
      <div class="appointment-row"><span>Date</span><span class="appointment-row__line appointment-row__line--date"></span><span>Time</span><span class="appointment-row__line appointment-row__line--time"></span></div>
      <div class="appointment-row"><span>Date</span><span class="appointment-row__line appointment-row__line--date"></span><span>Time</span><span class="appointment-row__line appointment-row__line--time"></span></div>
      <div class="appointment-row"><span>Date</span><span class="appointment-row__line appointment-row__line--date"></span><span>Time</span><span class="appointment-row__line appointment-row__line--time"></span></div>
    </div>
    <p class="services">
      Vehicle Servicing <span class="dot">•</span> All Mechanical Repairs <span class="dot">•</span> Automotive Parts &amp; Supplies<br>
      Tyres &amp; Wheel Alignments <span class="dot">•</span> Automotive Diagnostics <span class="dot">•</span> Warrant of Fitness
    </p>
  </section>

  <section class="card card--contact" aria-label="Contact side">
    <div class="brand"><span class="brand__mark"></span>Ridgeback Prime Automotive</div>
    <div class="contact-body">
      <div class="person">
        <div class="person__name">Lachie Westergaard</div>
        <div class="person__role">Director</div>
        <div class="person__address">48 Marlow Lane, Kereru Bay 3592</div>
      </div>
      <div class="divider"></div>
      <ul class="contact-list">
        <li><svg viewBox="0 0 12 12" aria-hidden="true"><path d="M2 1h2.5l1 2.5-1.3 1a6 6 0 0 0 3.3 3.3l1-1.3L11 7.5V10a1 1 0 0 1-1 1A9 9 0 0 1 1 2a1 1 0 0 1 1-1z" fill="var(--brand-red)"/></svg>07 842 1937</li>
        <li><svg viewBox="0 0 12 12" aria-hidden="true"><rect x="3" y="0.8" width="6" height="10.4" rx="1" fill="none" stroke="var(--brand-red)" stroke-width="1.2"/><circle cx="6" cy="9.3" r="0.7" fill="var(--brand-red)"/></svg>027 519 2764</li>
        <li><svg viewBox="0 0 12 12" aria-hidden="true"><rect x="0.8" y="2.2" width="10.4" height="7.6" fill="none" stroke="var(--brand-red)" stroke-width="1.2"/><path d="M1 2.6l5 4 5-4" fill="none" stroke="var(--brand-red)" stroke-width="1.2"/></svg>office@ridgebackmotors.co.nz</li>
        <li><svg viewBox="0 0 12 12" aria-hidden="true"><circle cx="6" cy="6" r="5.2" fill="none" stroke="var(--brand-red)" stroke-width="1.1"/><ellipse cx="6" cy="6" rx="2.2" ry="5.2" fill="none" stroke="var(--brand-red)" stroke-width="1"/><path d="M0.8 6h10.4" stroke="var(--brand-red)" stroke-width="1"/></svg>ridgebackmotors.co.nz</li>
      </ul>
    </div>
  </section>

</main>
</body>
</html>
```